Business Card for Restaurant Vendal

This project consist of creating 2 design for business card of restaurant named Vendal.

The attached specs below are 'ONLY SUGGESTION' if you have others ideas. You are welcome to post it.

1) Restaurant Card

Adresse:
2784 Côte du Pinard Vert
Montréal (Qc) H4K 3T8

Website:
www.ven-dal.ca

Phone:
438-719-2046

2) Employee Card

Name: Lorna Pik
Title: Owner

Address:
2784 Côte du Pinard Vert
Montréal (Qc) H4K 3T8

Email:lorna@ven-dal.ca
Phone Number:438-719-2046
Cellphone Number:514-830-4162

 The attached specs are 'ONLY SUGGESTION' if you have others ideas.  You are welcome to post it.

Industry/Entity Type

Restaurant

Requirements
Must have
• UV Card Spot

To print Spot UV business cards you would have to submit 2 files for each side. The first file "base" would be your regular design file as it would have been in any other case. The 2nd file "UV mask" is a black/white file. The BLACK color will indicate the areas that will be covered with the UV high gloss finish. To upload the files, please combine front design and front mask file in one P
Nice to have
• 1) The font of the logo should be ink effect
2) black background with wallpaper effect
3) The specs below are 'ONLY SUGGESTION' if you have others ideas. You are welcome to post it.

```html
<!DOCTYPE html>
<html lang="fr">
<head>
<meta charset="utf-8">
<title>Vendal — Business Cards</title>
<link rel="stylesheet" href="https://fonts.googleapis.com/css2?family=Open+Sans:wght@400;600;700&family=Noto+Sans+JP:wght@500;700&display=swap">
<style>
  :root {
    --page-bg: #ece9e4;
    --card-dark: #000000;
    --card-light: #ffffff;
    --brand-red: #e8312a;
    --lantern-red: #e0261d;
    --lantern-deep: #9c120c;
    --text-white: #ffffff;
    --text-dark: #1a1a1a;
  }
  * { box-sizing: border-box; margin: 0; padding: 0; }
  html, body {
    width: 1200px; height: 1000px; overflow: hidden;
    background: var(--page-bg);
  }
  .canvas { position: relative; width: 1200px; height: 1000px; }

  .card {
    position: absolute;
    width: 760px; height: 420px;
    box-shadow: 0 6px 18px rgba(0,0,0,0.18);
    overflow: hidden;
  }

  /* Front card */
  .card-front { left: 220px; top: 60px; background: var(--card-dark); }
  .front-lantern {
    position: absolute; left: 40px; top: 80px;
    width: 250px; height: 290px;
    border-radius: 48% 48% 46% 46%;
    background: radial-gradient(circle at 45% 35%, #ff4a3a 0%, var(--lantern-red) 45%, var(--lantern-deep) 90%, #3a0604 100%);
  }
  .brand-name {
    position: absolute; left: 318px; top: 150px;
    width: 350px;
    font-family: "Open Sans", sans-serif; font-weight: 700;
    font-size: 96px; line-height: 1; letter-spacing: 1px;
    color: var(--text-white);
    white-space: nowrap;
  }
  .brand-kana {
    position: absolute; left: 688px; top: 168px;
    writing-mode: vertical-rl;
    font-family: "Noto Sans JP", sans-serif; font-weight: 500;
    font-size: 32px; line-height: 1; letter-spacing: 4px;
    color: var(--brand-red);
  }
  .tagline {
    position: absolute; left: 322px; top: 292px;
    font-family: "Open Sans", "Noto Sans JP", sans-serif; font-weight: 400;
    font-size: 17px; color: var(--text-white); letter-spacing: 0.3px;
    white-space: nowrap;
  }
  .tagline .dot { color: var(--brand-red); margin: 0 6px; }

  /* Back card */
  .card-back { left: 200px; top: 540px; height: 400px; background: var(--card-light); }
  .back-header {
    position: absolute; left: 44px; top: 48px;
    display: flex; align-items: center; gap: 14px;
  }
  .back-header svg { width: 58px; height: 52px; }
  .back-kana {
    font-family: "Noto Sans JP", sans-serif; font-weight: 700;
    font-size: 40px; color: var(--brand-red); letter-spacing: 2px;
  }
  .contact-list { position: absolute; left: 90px; top: 170px; list-style: none; }
  .contact-item {
    display: flex; align-items: center; gap: 34px;
    font-family: "Open Sans", sans-serif; font-size: 17px;
    color: var(--text-dark); line-height: 1.4;
    margin-bottom: 26px;
  }
  .contact-item svg { width: 30px; height: 30px; flex: none; }
  .back-lantern {
    position: absolute; left: 490px; top: 70px;
    width: 230px; height: 280px;
    border-radius: 48% 48% 44% 44%;
    background: radial-gradient(circle at 45% 40%, #ff5a48 0%, var(--lantern-red) 55%, #f7b1a8 92%, #ffffff 100%);
  }
</style>
</head>
<body>
<main class="canvas">

  <section class="card card-front">
    <div class="front-lantern" role="img" aria-label="Illustration of a red paper lantern with a white brush-stroke handle"></div>
    <div class="brand-name">Vendal</div>
    <div class="brand-kana">ベンダル</div>
    <p class="tagline">Resto-Bar Japonais<span class="dot">•</span>Izakaya<span class="dot">•</span>居酒屋</p>
  </section>

  <section class="card card-back">
    <div class="back-header">
      <svg viewBox="0 0 58 52" aria-hidden="true">
        <path d="M29 3 L3 26 L10 26 L10 49 L23 49 L23 34 L35 34 L35 49 L48 49 L48 26 L55 26 Z" fill="var(--brand-red)"/>
      </svg>
      <span class="back-kana">ベンダル</span>
    </div>

    <ul class="contact-list">
      <li class="contact-item">
        <svg viewBox="0 0 30 30" aria-hidden="true">
          <path d="M15 2 C9 2 5 6.5 5 12 C5 19 15 28 15 28 C15 28 25 19 25 12 C25 6.5 21 2 15 2 Z" fill="var(--brand-red)"/>
          <circle cx="15" cy="12" r="4" fill="#fff"/>
        </svg>
        <span>2784 Côte du Pinard Vert<br>Montréal (Qc) H4K 3T8</span>
      </li>
      <li class="contact-item">
        <svg viewBox="0 0 30 30" aria-hidden="true">
          <rect x="1" y="1" width="28" height="28" rx="6" fill="var(--brand-red)"/>
          <circle cx="15" cy="15" r="8" fill="none" stroke="#fff" stroke-width="1.6"/>
          <ellipse cx="15" cy="15" rx="3.5" ry="8" fill="none" stroke="#fff" stroke-width="1.4"/>
          <line x1="7" y1="15" x2="23" y2="15" stroke="#fff" stroke-width="1.4"/>
        </svg>
        <span>www.ven-dal.ca</span>
      </li>
      <li class="contact-item">
        <svg viewBox="0 0 30 30" aria-hidden="true">
          <path d="M8 3 L12 3 L14 10 L11 12 C12.5 16 14 17.5 18 19 L20 16 L27 18 L27 22 C27 25 25 27 22 27 C12 26 4 18 3 8 C3 5 5 3 8 3 Z" fill="var(--brand-red)"/>
        </svg>
        <span>438-719-2046</span>
      </li>
    </ul>

    <div class="back-lantern" role="img" aria-label="Illustration of a red lantern with a black brush handle and the brushed characters 居酒屋"></div>
  </section>

</main>
</body>
</html>
```